Business and Success Coaching Business Card

Need a business card for my coaching business. I coach small businesses, career professionals and, individuals wanting to unlock their human potential and achieve excellence. At the heart of our methodology is the Shaping Purposeful Action Routines Knowingly (SPARK) approach to formulate empowerment, create principles for success and setting achievable outcomes. I would like something that incorporates our new logo, something clean and sharp with a solid darker, but complementary background, color on the card front. The back should be white where there will be room for three questions

Target Market(s)

People looking to advance and improve themselves through a success coach

Industry/Entity Type

Life Coaching

Contact Information for Business Card

Contact information on card.
Business name on front of card
Questions on back

Font styles to use
Other font styles liked:
• Century Gothic or other Serif style fonts that look similar to Century Gothic

Colors

Designer to choose colors to be used in the design.

Requirements
Must have
• Logo on front of card
• Business name - The Steady Forge
• Contact name - Ted Harlow
• Address - Box 4619, Maple Ridge, OR 97302-4619
• Phone number - 303-555-0147
• Email address - harlow.ted@thesteadyforge.example
• Certifications - ACT, SRC, LMP, GCF
• Back of card
• Three questions on the back of the card:
• If you were at your best, what would you do right now?
• What is the decision you have been avoiding?
• What's one action you could take in the next 10 minutes?
Nice to have
• I would like to see a solid color on the front of the card that compliments the logo.
• Back should be white, or could be contrasting, but need to have the three questions.

```html
<!DOCTYPE html>
<html lang="en">
<head>
<meta charset="utf-8">
<title>The Steady Forge – Business Card</title>
<link href="https://fonts.googleapis.com/css2?family=Montserrat:wght@300;400;600;700&display=swap" rel="stylesheet">
<style>
  :root {
    --sky: #1eaaf1;
    --sky-deep: #0d8fd8;
    --navy: #0f1d4a;
    --white: #ffffff;
    --muted: #b9c6e4;
    --stage: #2b2d31;
  }
  * { box-sizing: border-box; margin: 0; padding: 0; }
  html, body {
    width: 1200px; height: 900px; overflow: hidden;
    background: var(--stage);
    font-family: "Montserrat", "Century Gothic", sans-serif;
  }
  .card {
    position: absolute;
    width: 600px; height: 343px;
    overflow: hidden;
    box-shadow: 0 14px 30px rgba(0,0,0,.45);
  }
  .card-front { left: 70px; top: 70px; background: var(--sky); }
  .card-back { left: 530px; top: 487px; background: linear-gradient(160deg, var(--sky) 0%, var(--sky-deep) 100%); }
  .card svg.shape { position: absolute; inset: 0; width: 100%; height: 100%; }

  .logo-mark {
    position: absolute; width: 54px; height: 54px; border-radius: 50%;
    background: var(--navy);
  }
  .card-front .logo-mark { left: 150px; top: 62px; }
  .card-back .logo-mark { left: 500px; top: 58px; }

  .brand { position: absolute; left: 222px; top: 52px; color: var(--white); }
  .brand-name { font-size: 34px; font-weight: 700; letter-spacing: .2px; line-height: 1; }
  .brand-tagline { font-size: 14px; font-weight: 400; margin-top: 6px; padding-left: 40px; }

  .person { position: absolute; right: 34px; top: 146px; text-align: left; }
  .person-name { color: var(--muted); font-size: 16px; font-weight: 600; }
  .person-cert-label { color: var(--muted); font-size: 11px; font-weight: 400; margin-top: 6px; padding-left: 20px; }
  .person-certs { color: var(--muted); font-size: 11px; font-weight: 300; margin-top: 2px; }

  .contact { position: absolute; left: 250px; top: 236px; list-style: none; color: var(--white); font-size: 14px; font-weight: 400; }
  .contact li { display: flex; align-items: center; gap: 8px; line-height: 1.55; }
  .contact svg { width: 12px; height: 12px; fill: none; stroke: var(--sky); stroke-width: 2; flex: none; }
  .contact .icon-fill { fill: var(--sky); stroke: none; }

  .questions { position: absolute; left: 0; top: 34px; list-style: none; }
  .question { position: relative; height: 82px; }
  .question-text {
    position: relative; padding-left: 56px; color: var(--navy);
    font-size: 17px; font-weight: 700; line-height: 1.15;
  }
  .question-text .tick { position: absolute; left: 30px; top: 1px; color: var(--white); font-size: 22px; }
  .question-bar { position: absolute; left: 0; top: 44px; width: 470px; height: 28px; background: var(--white); clip-path: polygon(0 0, 100% 0, 94% 100%, 0 100%); }
</style>
</head>
<body>

<section class="card card-front" aria-label="Card front">
  <svg class="shape" viewBox="0 0 600 343" preserveAspectRatio="none" aria-hidden="true">
    <path d="M0 343 L0 312 C70 300 120 250 170 200 C210 160 250 140 320 140 L600 140 L600 343 Z" fill="var(--navy)"/>
  </svg>
  <div class="logo-mark" role="img" aria-label="The Steady Forge logo mark"></div>
  <div class="brand">
    <h1 class="brand-name">The Steady Forge</h1>
    <p class="brand-tagline">Build your next chapter</p>
  </div>
  <div class="person">
    <p class="person-name">Ted Harlow</p>
    <p class="person-cert-label">Certifications</p>
    <p class="person-certs">ACT, SRC, LMP, GCF</p>
  </div>
  <ul class="contact">
    <li><svg viewBox="0 0 12 12"><path d="M2 1 L4.5 1 L5 4 L3.6 5 C4.4 6.8 5.4 7.8 7 8.4 L8 7 L11 7.5 L11 10 C6 11 1 6 2 1 Z" class="icon-fill"/></svg>303-555-0147</li>
    <li><svg viewBox="0 0 12 12"><rect x="1" y="2.5" width="10" height="7"/><path d="M1 2.5 L6 6.5 L11 2.5"/></svg>harlow.ted@thesteadyforge.example</li>
    <li><svg viewBox="0 0 12 12"><path class="icon-fill" d="M6 0.5 C3.5 0.5 2 2.3 2 4.3 C2 7 6 11.5 6 11.5 C6 11.5 10 7 10 4.3 C10 2.3 8.5 0.5 6 0.5 Z M6 3 A1.3 1.3 0 1 0 6 5.6 A1.3 1.3 0 1 0 6 3 Z"/></svg>Box 4619, Maple Ridge, OR 97302-4619</li>
  </ul>
</section>

<section class="card card-back" aria-label="Card back">
  <svg class="shape" viewBox="0 0 600 343" preserveAspectRatio="none" aria-hidden="true">
    <path d="M600 90 C560 100 540 130 520 170 C505 200 470 250 430 300 L0 300 L0 343 L600 343 Z" fill="var(--navy)"/>
  </svg>
  <div class="logo-mark" role="img" aria-label="The Steady Forge logo mark"></div>
  <ol class="questions">
    <li class="question">
      <div class="question-bar"></div>
      <p class="question-text"><span class="tick">✓</span>If you were at your best,<br>what would you do right now?</p>
    </li>
    <li class="question">
      <div class="question-bar"></div>
      <p class="question-text"><span class="tick">✓</span>What is the decision<br>you have been avoiding?</p>
    </li>
    <li class="question">
      <div class="question-bar"></div>
      <p class="question-text"><span class="tick">✓</span>What's one action you could<br>take in the next 10 minutes?</p>
    </li>
  </ol>
</section>

</body>
</html>
```